business card design - photography

I am a fine art photographer. I would like to approach galleries to exhibit my work and need a business card.

The card should convey creativity and simplicity.
I would like a double sided card.

Some options:
1. An all white card with raised or embossed text or design to create a tactile finish.
2. a white and dark grey design would also work well.
3. Would be great to use my name as part of the design but not essential.
4. My name and title on the front, other details on the back of card.

The final design should be simple, minimal, elegant and innovative.
Being minimal, it will be more about texture, text size and placement.

examples of designs I would prefer provided here:
http://plimvarka.com/ideas/40-quiet-and-refined-card-layouts

I'm also open to other designs that may be unusual and unique.

Love this:
http://www.snapvelo.com/pics/morningverselog/583014927
Updates

I have uploaded a psd file after playing around in photoshop with various fonts.  I like the font (which I downloaded from glyphmorra.com called Arual) but the design probably needs some refining.  I hope this helps.  If you'd like me to change the format of the file, please let me know.

Ilvane

Target Market(s)

Art Gallery owners/administrators and customers.

Industry/Entity Type

Business

Requirements
Must have
• A unique look.

Matte, silky finish or heavy textured stock. Double-sided card.

Front:
my name
photography by

Back:
phone no
email
web address
Nice to have
• Letterpress
embrossed
Clean fonts
Should not have
• Do not use illustrations of cameras or lenses.
No frames around the card edge.

```html
<!DOCTYPE html>
<html lang="en">
<head>
<meta charset="utf-8">
<title>Ilvane Vestmar – Business Card Back</title>
<link rel="stylesheet" href="https://fonts.googleapis.com/css2?family=Arimo:wght@400;700&display=swap">
<style>
  :root {
    --card-grey: #404040;
    --accent-orange: #f39200;
    --accent-shadow: rgba(120, 60, 0, 0.55);
    --accent-highlight: rgba(255, 210, 120, 0.35);
  }
  html, body {
    margin: 0;
    padding: 0;
    width: 1200px;
    height: 734px;
    overflow: hidden;
    background: var(--card-grey);
  }
  .card-back {
    position: relative;
    width: 1200px;
    height: 734px;
    background: var(--card-grey);
    font-family: "Arimo", "Helvetica Neue", Helvetica, Arial, sans-serif;
  }
  .contact-list {
    position: absolute;
    left: 37px;
    bottom: 22px;
    margin: 0;
    padding: 0;
    list-style: none;
  }
  .contact-item {
    font-size: 52px;
    line-height: 68px;
    color: var(--accent-orange);
    white-space: nowrap;
    text-shadow: 0 -1px 0 var(--accent-highlight), 0 1px 1px var(--accent-shadow);
  }
  .contact-label {
    font-weight: 700;
  }
  .contact-value {
    font-weight: 400;
  }
</style>
</head>
<body>
  <main class="card-back">
    <ul class="contact-list">
      <li class="contact-item"><span class="contact-label">Mobile:</span> <span class="contact-value">0412 587 930</span></li>
      <li class="contact-item"><span class="contact-label">Email:</span> <span class="contact-value">ivestmar@mailnest.com</span></li>
      <li class="contact-item"><span class="contact-label">Website:</span> <span class="contact-value">www.ilvanevestmar.com</span></li>
    </ul>
  </main>
</body>
</html>
```